Brellin Trade Partners - we are Asian sourcing agents

We are sourcing agents based in the USA and we act as sourcing agents for clients in throughout the world. We focus primarily on custom sewn goods. So basically companies who do not have the in-house expertise to do it themselves, come to us and have us find suitable factories in Asia to do the production. We are middlemen. We find the factories...quote the project...manage the quality control and then deliver the goods directly to our customer's door. We pride ourselves in making the communication very easy and precise.

Current page is www.brellintrade.example

I am not happy w/ the overall look. The spacing...the photos, the fonts...the design elements...the pictures. I want a cool, crisp design that conveys professionalism and clearly depicts/explains what we do.

Requirements
Must have
• use my logo....I like it...it was designed by someone on this website.
Nice to have
• a video/animation of the entire process would be wonderful. Showing initial contact with our office in the USA...then to my correspondence with my offices in Taiwan and in Hong Kong...and then back and fort w/ the customer.....and then between my people in Hong Kong/Taiwan with the local factories......and then a quote is generated and sent to my client......to samples being made and sent for approval.....to a PO being generated......to final samples being sent.....to the order being shipped and delivered to the clients warehouse. I was thinking of an animation showing arrows and text showing the back and forth communication and explaining how the process flows.

```html
<!DOCTYPE html>
<html lang="en">
<head>
<meta charset="utf-8">
<title>Brellin Trade Partners – Asian Outsourcing Made Easy</title>
<link href="https://fonts.googleapis.com/css2?family=Montserrat:wght@400;500;600;700;800&family=PT+Serif&family=Arimo&display=swap" rel="stylesheet">
<style>
:root{
  --navy:#1b2a78;
  --olive:#7b9a1c;
  --orange:#ef5a2a;
  --green:#8cc43c;
  --yellow:#f5d93e;
  --stone:#8a897f;
  --panel-grey:#e1e2e4;
  --text:#3c3c3c;
  --link-blue:#2a88d8;
  --white:#ffffff;
}
*{margin:0;padding:0;box-sizing:border-box}
html,body{width:1200px;height:1190px;overflow:hidden}
body{position:relative;background:var(--stone);font-family:"Montserrat",sans-serif;color:var(--text)}
.site-header{position:absolute;left:0;top:0;width:1200px;height:176px;background:var(--white)}
.brand{position:absolute;left:108px;top:70px;display:flex;align-items:center;gap:10px}
.brand-mark{width:22px;height:22px;background:var(--navy)}
.brand-name{font-size:30px;font-weight:800;color:var(--navy);letter-spacing:.5px}
.main-nav{position:absolute;right:95px;top:112px;display:flex;gap:20px;font-size:15.5px;font-weight:500;letter-spacing:.6px}
.main-nav a{color:var(--navy);text-decoration:none}
.main-nav a.active{color:var(--olive)}
.hero{position:absolute;left:0;top:176px;width:1200px;height:400px;
  background:radial-gradient(ellipse at 70% 30%,#d8d2c6 0%,rgba(216,210,198,0) 40%),
  radial-gradient(ellipse at 80% 85%,#d8102a 0%,#b50d22 30%,rgba(181,13,34,0) 60%),
  radial-gradient(ellipse at 30% 45%,#f2a66a 0%,#c06a3a 35%,rgba(120,60,40,0) 65%),
  linear-gradient(100deg,#6a4f45 0%,#4a3530 45%,#3a302c 70%,#5a2a2a 100%)}
.hero-copy{position:absolute;left:103px;top:110px;color:var(--white);text-shadow:0 2px 4px rgba(0,0,0,.45)}
.hero-title{font-size:44px;font-weight:600;line-height:48px}
.hero-sub{font-size:32px;font-weight:600;line-height:40px;letter-spacing:.5px}
.hero-tag{font-size:22px;font-weight:500;line-height:22px;margin-top:10px;padding-left:4px}
.btn-quote{position:absolute;left:106px;top:271px;width:186px;height:48px;border-radius:6px;background:var(--orange);color:var(--white);font-size:17px;font-weight:700;letter-spacing:.5px;display:flex;align-items:center;justify-content:center}
.content{position:absolute;left:58px;top:575px;width:1074px;height:518px;background:var(--white)}
.category{position:absolute;top:35px;width:230px;text-align:center}
.category-photo{width:220px;height:150px;margin:0 auto;border-radius:4px}
.category h3{font-size:17px;font-weight:600;color:var(--orange);margin-top:20px}
.category p{font-size:11.5px;font-weight:500;line-height:16px;margin-top:20px;color:#444}
.quote-box{position:absolute;left:815px;top:31px;width:235px;height:286px;background:var(--green);color:var(--white);padding:16px 0 0 19px}
.quote-box h2{font-size:19px;font-weight:500;letter-spacing:.4px}
.quote-box p{font-size:14.5px;font-weight:500;line-height:22px;margin-top:10px;padding-left:4px}
.quote-box .contact{margin-top:16px;padding-left:10px}
.btn-request{position:absolute;left:29px;top:251px;width:176px;height:52px;border-radius:8px;background:var(--yellow);color:#222;font-size:17px;font-weight:500;display:flex;align-items:center;justify-content:center}
.know-box{position:absolute;left:23px;top:365px;width:766px;height:113px;background:var(--panel-grey);text-align:center}
.know-box h2{font-family:"PT Serif",serif;font-weight:400;font-size:17px;color:var(--link-blue);margin-top:20px;text-transform:uppercase}
.know-links{font-size:14px;font-weight:500;color:#555;line-height:24px;margin-top:10px}
.know-links span{margin:0 9px}
.solutions{position:absolute;left:808px;top:365px;width:239px;height:119px;background:var(--yellow);border-radius:6px;text-align:center;color:#222}
.solutions h2{font-size:17px;font-weight:500;margin-top:20px;letter-spacing:.3px}
.solutions p{font-size:13px;font-weight:500;line-height:21px;margin-top:6px;padding:0 18px;word-spacing:3px}
.site-footer{position:absolute;left:103px;top:1114px;color:var(--white);font-family:"Arimo",sans-serif;font-size:12.5px;line-height:20px}
.social{position:absolute;left:962px;top:1124px;display:flex;gap:22px}
.social span{width:20px;height:20px;border-radius:50%;background:#d4d3cc}
</style>
</head>
<body>
<header class="site-header">
  <div class="brand"><span class="brand-mark"></span><span class="brand-name">Brellin Trade Partners</span></div>
  <nav class="main-nav">
    <a class="active" href="#">HOME</a>
    <a href="#">PRODUCT CATEGORIES</a>
    <a href="#">ABOUT US</a>
    <a href="#">REQUEST QUOTE</a>
  </nav>
</header>

<section class="hero" role="img" aria-label="Close-up photo of hands guiding red fabric through a sewing machine">
  <div class="hero-copy">
    <div class="hero-title">Asian Outsourcing</div>
    <div class="hero-sub">MADE EASY!</div>
    <div class="hero-tag">Custom Sewn Goods Made<br>to Your Specifications</div>
  </div>
  <div class="btn-quote">GET A QUOTE</div>
</section>

<main class="content">
  <div class="category" style="left:32px">
    <div class="category-photo" role="img" aria-label="Photo of a black, grey and red messenger bag" style="background:linear-gradient(100deg,#2a2a2a 0%,#3a3a3a 40%,#8a8a8a 55%,#c8232a 65%,#3a3a3a 80%,#2a2a2a 100%)"></div>
    <h3>Bags</h3>
    <p>Need to spread the word to customers? Try Public Relations, Press Releases, and Media Kits to help reporters get the facts...when you speak at events or interviews.</p>
  </div>
  <div class="category" style="left:302px">
    <div class="category-photo" role="img" aria-label="Photo of a row of colourful phone cases" style="background:linear-gradient(90deg,#222 0%,#222 16%,#2a3fd0 16%,#2a3fd0 32%,#6a2ac0 32%,#6a2ac0 48%,#c02ab0 48%,#c02ab0 64%,#d8202a 64%,#d8202a 80%,#f0a020 80%,#f0a020 100%)"></div>
    <h3>Cases</h3>
    <p>Need help with social media? Want your own book on Bookvale? Let our creative marketing communication pros help you.. Go to Books &amp; Blogs.</p>
  </div>
  <div class="category" style="left:560px">
    <div class="category-photo" role="img" aria-label="Photo of a group of red, white and black golf bags" style="background:linear-gradient(90deg,#3a3a3a 0%,#c8202a 20%,#e8e8e8 45%,#f4f4f4 55%,#c8202a 75%,#3a3a3a 100%)"></div>
    <h3>Sporting Goods</h3>
    <p>Do you treat your employees like an audience? They are! Our employee relations, employee career skills and talent development programs have helped businesses grow.</p>
  </div>

  <aside class="quote-box">
    <h2>REQUEST A QUOTE</h2>
    <p>Please contact us for immediate consultation regarding your outsourcing project.</p>
    <p class="contact">Tel: 555-014-2210<br>Fax: 555-014-2211<br>Email:<br>info@brellintrade.example</p>
    <div class="btn-request">Request Quote</div>
  </aside>

  <section class="know-box">
    <h2>What You Need to Know</h2>
    <div class="know-links">
      <span>Contract Sewing in China</span><span>What is the Process?</span><span>What the Minimum Order?</span><br>
      <span>Contract Outsourcing FAQ</span><span>Outsourcing Case Study</span><span>Custom Industrial Sewing in China</span>
    </div>
  </section>

  <aside class="solutions">
    <h2>SOURCING SOLUTIONS</h2>
    <p>Bags Cases Covers Gloves Medical Sewn Goods Sporting Goods</p>
  </aside>
</main>

<footer class="site-footer">
  © 2015 Brellin<br>
  Home - Site Map – FAQ – Privacy Policy – Terms of Use – Contact Us
</footer>
<div class="social" aria-label="Social links"><span></span><span></span><span></span><span></span></div>
</body>
</html>
```